Improving a camping website homepage header*

My client is very happy with his new website and its new functionalities. However, he's not very happy about the homepage design. Specifically, the header(this includes the menu, large header image and two columns beneath that). You can find the website here: http://linkhop.example/tentsiteDemo .

He forwarded me several other websites he likes. Which can be found in the attachments. I also included several pictures of the camping.

I'm looking for a design that will improve the header of the homepage with room for other global style chances. The logo cannot be changed.

Attachments
1) His old website homepage
2) Website mockup he liked.
3) Another website mockup he liked.

Other images can be found on the new website http://linkhop.example/tentsiteDemo or his old website http://linkhop.example/priorTentsiteDemo.

Can you help us?
Updates

Hello guys. Here's a bit more information - Language used on the website is dutch. - The two columns left/right are supposed to link to Hire/Buy chalets. The client indicated that he finds these links important, but doesn't like the current design. I think this is partially the case because he doesn't like the icons. I'm looking forward to your designs!

Target Market(s)

30-50 year old wealthy people that want to purchase or rent cabins in the Netherlands.

Number of Pages Required

1 page

Colors

Designer to choose colors to be used in the design.

Requirements
Must have
• Improved header
Nice to have
• Global style changes
Should not have
• Logo changes

```html
<!DOCTYPE html>
<html lang="nl">
<head>
<meta charset="utf-8">
<title>Parc Lindenhove</title>
<link href="https://fonts.googleapis.com/css2?family=Open+Sans:wght@400;600;700&display=swap" rel="stylesheet">
<style>
:root{
  --green:#85bf00;
  --green-dark:#6fa300;
  --orange:#e8870a;
  --price:#f39200;
  --tag-sand:#f0c58a;
  --tag-blue:#2aa6dc;
  --ink:#222;
  --text:#444;
  --muted:#8a8a8a;
  --line:#e4e4e4;
  --white:#fff;
}
*{box-sizing:border-box;margin:0;padding:0}
html,body{width:1136px;height:1200px;overflow:hidden;background:var(--white);font-family:"Open Sans",sans-serif;color:var(--text)}
.page{position:relative;width:1136px;height:1200px}

.topbar{height:31px;background:var(--green);display:flex;align-items:center;justify-content:space-between;padding:0 106px 0 130px}
.topbar__phone{color:var(--white);font-size:12px;display:flex;align-items:center;gap:10px}
.topbar__login{background:var(--orange);color:var(--white);font-size:12px;font-weight:600;height:31px;padding:0 16px;display:flex;align-items:center}

.header{height:76px;display:flex;align-items:center;padding:0 106px 0 126px;justify-content:space-between}
.brand{display:flex;align-items:center;gap:10px}
.brand__dot{width:30px;height:30px;border-radius:50%;background:var(--green)}
.brand__name{font-size:20px;font-weight:600;color:var(--green-dark)}
.nav{display:flex;height:76px}
.nav a{position:relative;display:flex;align-items:center;padding:0 16px;font-size:14px;color:var(--ink);text-decoration:none}
.nav a.is-active{color:var(--green)}
.nav a.is-active::after{content:"";position:absolute;left:11px;right:11px;bottom:0;height:6px;background:var(--green)}

.hero{position:relative;height:459px;background:linear-gradient(180deg,#dfe8ea 0%,#6f8f55 30%,#3f6b63 55%,#7b9a6a 80%,#b5a77f 100%);text-align:center;color:var(--white)}
.hero__title{padding-top:158px;font-size:41px;font-weight:700;letter-spacing:1px;line-height:1}
.hero__title span{color:var(--green)}
.hero__rule{width:100px;height:2px;background:var(--white);margin:16px auto 20px}
.hero__lead{width:420px;margin:0 auto;font-size:13px;font-weight:600;line-height:19px}

.cta{position:absolute;top:518px;width:422px;height:149px;background:var(--white);box-shadow:0 4px 10px rgba(0,0,0,.08);padding:28px 26px 0 102px}
.cta--rent{left:127px}
.cta--buy{left:601px}
.cta__icon{position:absolute;left:-13px;top:32px;width:86px;height:76px;background:var(--green);display:flex;align-items:center;justify-content:center}
.cta__title{font-size:20px;font-weight:600;color:var(--ink);letter-spacing:.5px;margin-bottom:10px}
.cta__text{font-size:13px;line-height:16px;color:var(--muted)}

.recent{position:absolute;top:726px;left:76px;width:984px}
.recent__title{font-size:25px;font-weight:400;color:var(--ink);margin-bottom:20px}
.listings{display:flex;gap:28px}
.listing{width:309px;height:368px;border:1px solid var(--line);position:relative}
.listing__photo{height:193px;position:relative}
.photo--a{background:linear-gradient(180deg,#d9dfe3 0%,#9aa6a4 45%,#4f6b3a 80%,#3a5a2c 100%)}
.photo--b{background:linear-gradient(180deg,#9fb7c9 0%,#7c9b5e 40%,#c9c8b8 60%,#3e6530 100%)}
.photo--c{background:linear-gradient(180deg,#eef0f0 0%,#8b5a34 35%,#a86b3c 60%,#4a4d44 100%)}
.tag{position:absolute;top:18px;font-size:11px;padding:1px 8px;color:var(--ink)}
.tag--featured{left:18px;background:var(--tag-sand)}
.tag--type{right:18px;background:var(--tag-blue);color:var(--white);padding:1px 12px}
.tag--sold{right:30px;background:none;color:var(--white);top:18px}
.photo-count{position:absolute;right:18px;bottom:10px;color:var(--white);font-size:11px;display:flex;align-items:center;gap:3px}
.listing__body{padding:18px 18px 0}
.listing__name{font-size:16px;color:var(--ink);margin-bottom:8px}
.listing__price{font-size:15px;color:var(--price);margin-bottom:10px}
.listing__note{font-size:12px;color:var(--muted);margin-top:-2px;margin-bottom:6px}
.specs{display:flex;align-items:center;font-size:11px;color:var(--muted);gap:12px}
.spec{display:flex;align-items:center;gap:4px}
.more{margin-left:auto;background:var(--tag-sand);color:var(--white);font-size:11px;padding:1px 6px}
.listing__foot{position:absolute;left:18px;right:18px;bottom:0;height:52px;border-top:1px solid var(--line);display:flex;align-items:center}
.avatar{width:26px;height:26px;border-radius:50%;background:#7f9270;margin-right:10px}
.avatar--empty{background:#d6d6d6}
.author{font-size:12px;color:var(--muted)}
.actions{margin-left:auto;display:flex;gap:5px}
.action{width:26px;height:26px;border:1px solid var(--line);display:flex;align-items:center;justify-content:center}
</style>
</head>
<body>
<div class="page">
  <div class="topbar">
    <div class="topbar__phone">
      <svg width="13" height="13" viewBox="0 0 24 24"><path fill="#fff" d="M6.6 10.8a15 15 0 006.6 6.6l2.2-2.2c.3-.3.7-.4 1-.2 1.1.4 2.3.6 3.6.6.6 0 1 .4 1 1V20c0 .6-.4 1-1 1C10.6 21 3 13.4 3 4c0-.6.4-1 1-1h3.5c.6 0 1 .4 1 1 0 1.2.2 2.4.6 3.6.1.3 0 .7-.2 1z"/></svg>
      Call us today : 0300 - 12 34 56
    </div>
    <div class="topbar__login">Login / Sign up</div>
  </div>

  <header class="header">
    <div class="brand">
      <div class="brand__dot"></div>
      <div class="brand__name">Parc Lindenhove</div>
    </div>
    <nav class="nav">
      <a class="is-active">Home</a>
      <a>Hetpark</a>
      <a>Financiering</a>
      <a>Chalets</a>
      <a>Aanbidingen</a>
      <a>Faciliteiten</a>
      <a>Contact</a>
    </nav>
  </header>

  <section class="hero" role="img" aria-label="Luchtfoto van het park met meer, zandstrand, parasols en chalets tussen de bomen">
    <h1 class="hero__title">PARC <span>LINDENHOVE</span></h1>
    <div class="hero__rule"></div>
    <p class="hero__lead">Lorem ipsum dolor sit amet, consectetur adipiscing elit. Aenean euismod bibendum laoreet. Proin gravida dolor sit amet lacus accumsan et viverra justo commodo.</p>
  </section>

  <a class="cta cta--rent">
    <div class="cta__icon">
      <svg width="48" height="42" viewBox="0 0 48 42"><path d="M24 3L3 21h6v18h12V28h6v11h12V21h6z" fill="none" stroke="#fff" stroke-width="4" stroke-linejoin="round"/></svg>
    </div>
    <h2 class="cta__title">CHALET HUREN</h2>
    <p class="cta__text">Lorem ipsum dolor sit amet, consectetur adipi-scing elit. Aenean euismod bibendum laoreet. Proin gravida dolor sit amet lacus accumsan.</p>
  </a>
  <a class="cta cta--buy">
    <div class="cta__icon">
      <svg width="52" height="42" viewBox="0 0 52 42"><rect x="6" y="14" width="40" height="24" rx="2" fill="none" stroke="#fff" stroke-width="4"/><circle cx="26" cy="26" r="5" fill="#fff"/><path d="M10 10L38 3l3 8" fill="none" stroke="#fff" stroke-width="3"/></svg>
    </div>
    <h2 class="cta__title">CHALET KOPEN</h2>
    <p class="cta__text">Lorem ipsum dolor sit amet, consectetur adipi-scing elit. Aenean euismod bibendum laoreet. Proin gravida dolor sit amet lacus accumsan.</p>
  </a>

  <section class="recent">
    <h2 class="recent__title">Recente Chalets</h2>
    <div class="listings">
      <article class="listing">
        <div class="listing__photo photo--a" role="img" aria-label="Wit houten chalet met terras en tuin">
          <span class="tag tag--featured">Aanbevolen</span>
          <span class="tag tag--type">Huren</span>
          <span class="photo-count"><svg width="12" height="10" viewBox="0 0 12 10"><rect x="0" y="2" width="12" height="8" rx="1" fill="#fff"/><circle cx="6" cy="6" r="2" fill="#777"/></svg>1</span>
        </div>
        <div class="listing__body">
          <h3 class="listing__name">Kavel 190</h3>
          <p class="listing__price">€ 350 per maand</p>
          <div class="specs">
            <span class="spec"><svg width="16" height="8"><rect x="0" y="3" width="16" height="4" fill="none" stroke="#aaa"/></svg>1</span>
            <span class="spec"><svg width="14" height="9"><path d="M1 3h12v3a3 3 0 01-3 3H4a3 3 0 01-3-3z" fill="none" stroke="#aaa"/></svg>3</span>
            <span class="spec"><svg width="13" height="10"><path d="M1 9h11V1z" fill="none" stroke="#aaa"/></svg>105 000,00 m²</span>
            <span class="more">lees meer</span>
          </div>
        </div>
        <div class="listing__foot">
          <div class="avatar"></div><span class="author">admin</span>
          <div class="actions"><span class="action"><svg width="10" height="10"><circle cx="2" cy="5" r="1.5" fill="#bbb"/><circle cx="8" cy="2" r="1.5" fill="#bbb"/><circle cx="8" cy="8" r="1.5" fill="#bbb"/><path d="M2 5L8 2M2 5l6 3" stroke="#bbb"/></svg></span><span class="action"><svg width="10" height="9"><path d="M5 9L1 4.5a2.2 2.2 0 014-2.5 2.2 2.2 0 014 2.5z" fill="#bbb"/></svg></span><span class="action"><svg width="10" height="10"><path d="M5 0v10M0 5h10" stroke="#bbb" stroke-width="2"/></svg></span></div>
        </div>
      </article>

      <article class="listing">
        <div class="listing__photo photo--b" role="img" aria-label="Lichte stacaravan aan het water met groen">
          <span class="tag tag--featured">Aanbevolen</span>
          <span class="tag tag--type" style="right:118px">Kopen</span>
          <span class="tag tag--sold">Verkocht</span>
          <span class="photo-count"><svg width="12" height="10" viewBox="0 0 12 10"><rect x="0" y="2" width="12" height="8" rx="1" fill="#fff"/><circle cx="6" cy="6" r="2" fill="#777"/></svg>1</span>
        </div>
        <div class="listing__body">
          <h3 class="listing__name">Kavel 233</h3>
          <p class="listing__price">€ 205.000</p>
          <p class="listing__note">Ook een mooie chalet.</p>
          <div class="specs">
            <span class="spec"><svg width="16" height="8"><rect x="0" y="3" width="16" height="4" fill="none" stroke="#aaa"/></svg>1</span>
            <span class="spec"><svg width="14" height="9"><path d="M1 3h12v3a3 3 0 01-3 3H4a3 3 0 01-3-3z" fill="none" stroke="#aaa"/></svg>1</span>
            <span class="spec"><svg width="13" height="10"><path d="M1 9h11V1z" fill="none" stroke="#aaa"/></svg>130,00 m²</span>
            <span class="more">lees meer</span>
          </div>
        </div>
        <div class="listing__foot">
          <div class="avatar"></div><span class="author">admin</span>
          <div class="actions"><span class="action"><svg width="10" height="10"><circle cx="2" cy="5" r="1.5" fill="#bbb"/><circle cx="8" cy="2" r="1.5" fill="#bbb"/><circle cx="8" cy="8" r="1.5" fill="#bbb"/><path d="M2 5L8 2M2 5l6 3" stroke="#bbb"/></svg></span><span class="action"><svg width="10" height="9"><path d="M5 9L1 4.5a2.2 2.2 0 014-2.5 2.2 2.2 0 014 2.5z" fill="#bbb"/></svg></span><span class="action"><svg width="10" height="10"><path d="M5 0v10M0 5h10" stroke="#bbb" stroke-width="2"/></svg></span></div>
        </div>
      </article>

      <article class="listing">
        <div class="listing__photo photo--c" role="img" aria-label="Houten blokhut chalet met oprit">
          <span class="tag tag--featured">Aanbevolen</span>
          <span class="tag tag--type">Kopen</span>
          <svg style="position:absolute;left:18px;top:84px" width="14" height="26"><path d="M12 2L2 13l10 11" fill="none" stroke="#fff" stroke-width="2"/></svg>
          <svg style="position:absolute;right:18px;top:84px" width="14" height="26"><path d="M2 2l10 11L2 24" fill="none" stroke="#fff" stroke-width="2"/></svg>
          <span class="photo-count"><svg width="12" height="9"><rect x="0" y="1" width="8" height="7" fill="#fff"/><path d="M8 4.5l4-3v6z" fill="#fff"/></svg>&nbsp;<svg width="12" height="10" viewBox="0 0 12 10"><rect x="0" y="2" width="12" height="8" rx="1" fill="#fff"/><circle cx="6" cy="6" r="2" fill="#777"/></svg>3</span>
        </div>
        <div class="listing__body">
          <h3 class="listing__name">Kavel 236</h3>
          <p class="listing__price">€ 195.000</p>
          <p class="listing__note">Prachtige locatie incl. video!</p>
          <div class="specs">
            <span class="spec"><svg width="16" height="8"><rect x="0" y="3" width="16" height="4" fill="none" stroke="#aaa"/></svg>3</span>
            <span class="spec"><svg width="14" height="9"><path d="M1 3h12v3a3 3 0 01-3 3H4a3 3 0 01-3-3z" fill="none" stroke="#aaa"/></svg>2</span>
            <span class="spec"><svg width="13" height="10"><path d="M1 9h11V1z" fill="none" stroke="#aaa"/></svg>100,00 m²</span>
            <span class="more">lees meer</span>
          </div>
        </div>
        <div class="listing__foot">
          <div class="avatar avatar--empty"></div><span class="author" style="color:#555">Naam Achternaam</span>
          <div class="actions"><span class="action"><svg width="10" height="10"><circle cx="2" cy="5" r="1.5" fill="#bbb"/><circle cx="8" cy="2" r="1.5" fill="#bbb"/><circle cx="8" cy="8" r="1.5" fill="#bbb"/><path d="M2 5L8 2M2 5l6 3" stroke="#bbb"/></svg></span><span class="action"><svg width="10" height="9"><path d="M5 9L1 4.5a2.2 2.2 0 014-2.5 2.2 2.2 0 014 2.5z" fill="#bbb"/></svg></span><span class="action"><svg width="10" height="10"><path d="M5 0v10M0 5h10" stroke="#bbb" stroke-width="2"/></svg></span></div>
        </div>
      </article>
    </div>
  </section>
</div>
</body>
</html>
```